Designing a new homepage for www.Pelmora.net

WEBSITE: www.pelmora.net

ABOUT THE WEBSITE
The Pelmora.net (PLM) website contains a large directory of over 50,000 international trade service providers that is not valued enough on the homepage (HP). Currently from the HP, the site appears as a general site about imports and exports (international trade). As a result, it contradicts the purpose and experience of the site.
The website is new and original for international trade online: it is a tool to find the best experts and professionals that can help importers and exporters to implement their overseas operations.

Specifically:
a) An exporter who wants to sell in Italy can find on PLM: agents to distribute their products, a lawyer for reviewing contracts, translators to translate brochures and websites, an export consultant, etc. Various local providers that can help sell their products in Italy, a local provider (e.g. based in Italy) are generally more efficient and less costly than a supplier in the exporter’s home country

b) An importer who wants to buy in China will find purchasing agents who source products for third parties; logistics companies that store and ship merchandise; corporate quality control to ensure product quality before shipment, etc.; various local providers based in China to better organize its import operation.

PLM is therefore a very resourceful solution for SMEs who want to develop, improve and organize their international trade:
a) it significantly increases their ability to create new opportunities by using the services of a third party: export to a new country; import a new product
b) it allows them to optimize their purchases of services by seeking alternatives: find a less expensive carrier, a foreign lawyer challenged by a local lawyer

It is the perfect complement to cross border marketplaces (e.g. Vuxentor.com, brimwellhub.com, zq48.com) which concentrate on the search for products (and of companies/counterparts) but:
a) help the user to import only, not really export
b) do not help implement the operations of exporting/importing from A to Z

Therefore, PLM offers a new way of “easy exporting” (or easy importing).

THE BRIEF

The objective of the project is to rethink the HP (and the site design) to highlight this experience: "export and import more successfully through 50,000+ service providers in over 100 countries”.
We have created a wireframe (see attached) of the structure we feel best meets this objective. What do you think? Do we meet it through our wireframe? Then, next step is to take this wireframe and create a clear design that really helps us to achieve our objective.

It is considered that the site captures the importers/exporters seeking to increase their exports or to better organize their imports (but we do not start from a priori that these users are looking for service providers).
The HP should highlight the importance of service providers addressing export markets or better organizing their imports; the "market analyses" of the site should act as a "knowledge resource", where the site offers more the main experience: if you want to export to a country you have any interest to first explore what the partners listed by PLM can provide.

Reason: We feel that we're seeing some interesting designs and would like to give current and even potential submissions more time. So far we have not seen the one that really strikes us, so perhaps more time is what we and the designers need! Thanks!

Target Market(s)

Importers, exporters, international trade service providers, foreign investors, etc

Industry/Entity Type

Lawyer

Requirements
Must have
• • Please use the current basic design elements of the website, including the logo, (www.pelmora.net). These include colors and fonts, etc. We only aim to change the HP and therefore, only implement a change to the header and footer of the whole site.
• Please find inspiration from our wireframes (attached), as they have been carefully thought about by our own team. However, should you feel the need to challenge the wireframes, please do so in your design, we're interested to see what you can present us.
• Our prime objective in terms of design: creating a more user-friendly interface on the HP to guide users into the rest of the website
• We already have a psd file based on the wireframes we’ve attached to the brief. If you would like this, so your job is easier (such as using same text as we have in the wireframes), let us know!

```html
<!DOCTYPE html>
<html lang="en">
<head>
<meta charset="utf-8">
<title>Pelmora.net – Improve your business overseas</title>
<link href="https://fonts.googleapis.com/css2?family=Arimo:ital,wght@0,400;0,700;1,400&family=Roboto+Condensed:wght@300;400&family=PT+Sans:wght@700&display=swap" rel="stylesheet">
<style>
:root{
  --page:#f3f2f0;
  --bar-top:#fafafa;
  --bar-bottom:#e2e2e2;
  --text:#222;
  --muted:#555;
  --soft:#8a8a8a;
  --link:#3a7fc1;
  --brand:#1f5f96;
  --headline:#3d8fd0;
  --beige-1:#e9e4dc;
  --beige-2:#d8d0c4;
  --line:#c9c2b6;
  --white:#fff;
}
*{box-sizing:border-box;margin:0;padding:0}
html,body{width:1200px;height:900px;overflow:hidden}
body{background:var(--page);font-family:"Arimo",Arial,sans-serif;color:var(--text);position:relative}
.abs{position:absolute}
a{color:var(--link)}

.topbar{left:0;top:0;width:1200px;height:31px;background:linear-gradient(var(--bar-top),var(--bar-bottom));border-bottom:1px solid #d0d0d0}
.topbar .link{position:absolute;top:9px;font-size:12px;color:#555}
.like-box{display:inline-block;width:11px;height:11px;border:1px solid #777;margin-right:4px;vertical-align:-1px}
.account{position:absolute;top:0;height:31px;font-size:11px;color:#222;text-align:center;line-height:31px;background:linear-gradient(#fff,#ececec);border-left:1px solid #d6d6d6}

.logo{left:172px;top:66px;font-size:24px;letter-spacing:8px;color:var(--brand);display:flex;align-items:center;gap:10px}
.logo .dot{width:26px;height:26px;border-radius:50%;background:var(--brand)}

.mainnav{top:131px;font-size:14px;font-weight:700;color:#3c3c3c;letter-spacing:.2px}
.sep{width:1px;height:40px;top:117px;background:var(--brand)}
.search{left:715px;top:123px;width:348px;height:29px;background:#fff;border:1px solid #d0d0d0;font-size:12px;color:#888;padding:7px 0 0 8px}
.search svg{position:absolute;right:8px;top:6px}

.hero{left:123px;top:165px;width:951px;height:351px;border:1px solid #ddd;overflow:hidden}
.hero-photo{position:absolute;inset:0;background:linear-gradient(100deg,#6e7a86 0%,#b9bec3 30%,#e8e6e2 55%,#d9dde0 75%,#c5ccd2 100%)}
.hero h1{position:absolute;left:25px;top:10px;font-family:"Roboto Condensed",sans-serif;font-weight:400;font-size:40px;color:var(--headline);letter-spacing:-.5px}
.hero .lead{position:absolute;left:25px;top:62px;font-family:"PT Sans",sans-serif;font-size:17px;color:#fff}
.hero ul{position:absolute;left:28px;top:86px;list-style:none;color:#fff;font-size:14px;line-height:23.5px}
.hero ul li::before{content:"• ";}
.hero .listed{position:absolute;left:23px;top:204px;color:#fff;font-size:12px;line-height:17px}
.badge{position:absolute;left:165px;top:200px;width:38px;height:46px;border-radius:4px;background:#4a4f57}
.action{position:absolute;left:0;top:266px;width:951px;height:71px;background:rgba(221,214,204,.9)}
.action .start{position:absolute;left:42px;top:18px;font-family:"Roboto Condensed",sans-serif;font-weight:300;font-size:30px;color:#fff}
.select{position:absolute;left:166px;top:18px;width:252px;height:38px;background:linear-gradient(#f4f2ee,#e3ded5);border:1px solid #bdb6aa;font-size:14px;font-weight:700;color:#aaa;padding:11px 0 0 23px}
.select b{color:var(--brand)}
.select .arrow{position:absolute;right:9px;top:9px;width:21px;height:20px;border:1px solid #bbb;background:#fafafa;font-size:9px;color:#888;text-align:center;line-height:20px;font-weight:400}
.action .find{position:absolute;left:435px;top:32px;font-size:14px;font-weight:700;color:#fff}
.opt{position:absolute;top:29px;font-size:16px;font-weight:700;color:#1e6fb8;display:flex;align-items:center;gap:6px}
.box{width:12px;height:12px;border:1px solid #888;background:#fff;display:inline-block}
.go{position:absolute;left:873px;top:18px;width:52px;height:37px;background:linear-gradient(#f7f5f1,#e3ddd3);font-size:24px;font-weight:700;color:#1e6fb8;text-align:center;line-height:37px}

.export{left:123px;top:533px;width:951px;height:193px;background:linear-gradient(var(--beige-2),var(--beige-1));border:1px solid #b6b2ad}
.export .nav{position:absolute;top:30px;font-size:13px;color:#3d8fd0}
.export h2{position:absolute;left:74px;top:18px;font-weight:400;font-size:28px;color:#222}
.export .discover{position:absolute;left:500px;top:31px;font-size:14px;color:#555}
.partner-logo{position:absolute;left:22px;top:89px;width:82px;height:82px;background:#fff;border:1px solid #ddd;display:flex;flex-direction:column;align-items:center;justify-content:center;gap:6px;font-size:11px;font-weight:700;color:#777}
.partner-logo i{width:22px;height:22px;border-radius:50%;border:2px solid #999;display:block}
.partner{position:absolute;left:129px;top:86px}
.partner strong{font-size:15px;display:block}
.partner .role{font-size:14px;color:#666;display:block;margin-top:2px}
.partner p{font-size:12px;color:#aaa;line-height:16px;margin-top:4px;width:330px}
.partner-links{position:absolute;left:130px;top:164px;width:317px;font-size:11px;display:flex;justify-content:space-between}
.divider{position:absolute;left:478px;top:91px;width:1px;height:80px;background:#bdb6aa}
.stat{position:absolute;top:82px;width:150px;text-align:center;color:#555}
.stat .num{font-size:44px;color:#666;line-height:46px}
.stat .what{font-size:14px;font-weight:700;margin-top:2px}
.stat .where{font-size:12px;margin-top:2px}
.stat a{font-size:13px;display:block;margin-top:3px}

.col-title{top:759px;font-size:16px;font-weight:700;color:#555}
.tab{top:793px;height:35px;font-size:15px;font-weight:700;color:#555;padding:9px 0 0 24px}
.tab.active{background:#fff;border:1px solid #ddd;border-bottom:none}
.tab.idle{background:#d8d3cb;padding-left:15px}
.dir-list{left:123px;top:828px;width:283px;height:80px;background:#fff;border:1px solid #ddd;border-top:none;list-style:none;padding:19px 0 0 13px;font-size:13px;color:#333;line-height:26px}
.dir-list li::before{content:"•";color:#666;margin-right:12px}
.panel{left:430px;top:793px;width:645px;height:120px;background:#e6e1d9}
.zone{left:437px;top:797px;width:85px;height:85px;background:#fff;border:1px solid #aaa}
.zone span{position:absolute;left:0;top:33px;width:100%;text-align:center;font-size:13px;color:#333}
.speaker{left:535px;top:824px}
.speaker .name{font-size:12px;font-weight:700;color:var(--link)}
.speaker .svc{font-size:14px;font-weight:700;color:#444;margin-top:3px}
.speaker .loc{font-size:14px;color:#555;margin-top:3px}
.quote{left:437px;top:886px;font-size:13px;font-style:italic;color:#444}
.new-logo{left:772px;top:809px;width:85px;height:85px;background:#fff;border:1px solid #ddd;display:flex;align-items:center;justify-content:center;font-size:13px;font-weight:700;color:#555}
.provider{left:863px;top:812px;width:205px}
.provider .name{font-size:12px;font-weight:700;color:var(--link)}
.provider .svc{font-size:11px;font-weight:700;color:#333;margin-top:2px}
.provider p{font-size:11px;color:#444;line-height:14px;margin-top:5px}
.provider a{display:block;text-align:right;font-size:11px;margin-top:6px;margin-right:14px}
</style>
</head>
<body>

<header class="abs topbar">
  <span class="link" style="left:122px">Home</span>
  <span class="link" style="left:183px">About us</span>
  <span class="link" style="left:257px">Take a tour</span>
  <span class="link" style="left:341px">Advertise</span>
  <span class="link" style="left:412px">Why Pelmora.net</span>
  <span class="link" style="left:548px"><span class="like-box"></span>Like</span>
  <span class="account" style="left:803px;width:60px">LOGIN</span>
  <span class="account" style="left:862px;width:75px">SIGN UP</span>
  <span class="account" style="left:936px;width:138px;border-right:1px solid #d6d6d6">LIST YOUR SERVICES</span>
</header>

<div class="abs logo"><span class="dot"></span>Pelmora.net</div>

<nav>
  <span class="abs mainnav" style="left:138px">ALL TRADE SERVICES</span>
  <span class="abs sep" style="left:301px"></span>
  <span class="abs mainnav" style="left:317px">LET US HELP YOU</span>
  <span class="abs sep" style="left:450px"></span>
  <span class="abs mainnav" style="left:469px">BROWSE KNOWLEDGE</span>
</nav>
<div class="abs search">Search 20,000+ content items &amp; 50,000+ services providers...
  <svg width="18" height="18" viewBox="0 0 18 18"><circle cx="7" cy="7" r="5" fill="none" stroke="#777" stroke-width="2"/><line x1="11" y1="11" x2="16" y2="16" stroke="#777" stroke-width="3"/></svg>
</div>

<section class="abs hero">
  <div class="hero-photo" role="img" aria-label="Photo of a team of business people working together at a desk"></div>
  <h1>Improve your business overseas!</h1>
  <div class="lead">Use the leverage of 51,000+ verified services providers:</div>
  <ul>
    <li>Sales agents, market entry, customs services</li>
    <li>Sourcing companies, freight forwarders, quality control</li>
    <li>Lawyers, accounting, expat services and more</li>
  </ul>
  <div class="listed">Includes the service<br>providers listed by:<br>• • •</div>
  <div class="badge" role="img" aria-label="Partner listing badge"></div>
  <div class="action">
    <span class="start">start now</span>
    <div class="select">select your <b>target country</b><span class="arrow">▼</span></div>
    <span class="find">and find asistancce to</span>
    <span class="opt" style="left:612px"><span class="box" style="position:relative"><svg width="10" height="10" viewBox="0 0 10 10" style="position:absolute;left:0;top:0"><path d="M1 5l3 3 5-7" fill="none" stroke="#333" stroke-width="1.5"/></svg></span>Import</span>
    <span class="opt" style="left:695px"><span class="box"></span>Export</span>
    <span class="opt" style="left:781px"><span class="box"></span>Invest</span>
    <span class="go">GO</span>
  </div>
</section>

<section class="abs export">
  <span class="nav" style="left:16px">◀</span>
  <span class="nav" style="left:921px">▶</span>
  <h2>Want to export to South Africa?</h2>
  <span class="discover">Discover 451 Service Providers to help you export including:</span>
  <div class="partner-logo"><i></i>MERIDEX</div>
  <div class="partner">
    <strong>Meridex South Africa</strong>
    <span class="role">Export support</span>
    <p>Lorem ipsum dolor sit amet, consectetur adipiscing elit. Integer vehicula, lectus at laoreet dignissim.</p>
  </div>
  <div class="partner-links"><a>www.meridex-sa.com</a><a>Want your logo here?</a></div>
  <span class="divider"></span>
  <div class="stat" style="left:492px"><div class="num">25</div><div class="what">Freight Forwarders</div><div class="where">in South Africa</div><a>See all</a></div>
  <div class="stat" style="left:648px"><div class="num">47</div><div class="what">Corporate Lawyers</div><div class="where">in South Africa</div><a>See all</a></div>
  <div class="stat" style="left:798px"><div class="num">56</div><div class="what">Debt Collectors</div><div class="where">in South Africa</div><a>See all</a></div>
</section>

<svg class="abs" style="left:148px;top:755px" width="26" height="26" viewBox="0 0 26 26"><circle cx="10" cy="10" r="7" fill="#fff" stroke="#888" stroke-width="2"/><line x1="15" y1="15" x2="23" y2="23" stroke="#666" stroke-width="4" stroke-linecap="round"/></svg>
<span class="abs col-title" style="left:185px">Browse Our Directory</span>
<span class="abs col-title" style="left:477px">What Importers / Exporters Say</span>
<span class="abs col-title" style="left:853px;top:761px">New Service Providers</span>

<div class="abs tab active" style="left:123px;width:143px">Services 200+</div>
<div class="abs tab idle" style="left:265px;width:141px">Countries 100+</div>
<ul class="abs dir-list">
  <li>Freight Forwarders (7843)</li>
  <li>Trading Companies (2489)</li>
</ul>

<div class="abs panel"></div>
<div class="abs zone">
  <svg width="83" height="83" viewBox="0 0 83 83" style="position:absolute;left:0;top:0"><line x1="0" y1="0" x2="83" y2="83" stroke="#999"/><line x1="83" y1="0" x2="0" y2="83" stroke="#999"/></svg>
  <span>Zone image</span>
</div>
<div class="abs speaker">
  <div class="name">Name Of Speaker</div>
  <div class="svc">Sourcing Services</div>
  <div class="loc">Florida, The United States</div>
</div>
<div class="abs quote">“ Lorem ipsum dolor sit amet, consectetur adipi-</div>

<div class="abs new-logo">Korvane</div>
<div class="abs provider">
  <div class="name">Korvane Media Limited</div>
  <div class="svc">Tax Services in the United Kingdom</div>
  <p>Lorem ipsum dolor sit amet, consectetur adipiscing elit dolo lectus at laoreet...</p>
  <a>View profile</a>
</div>

</body>
</html>
```